Modern & Fresh Halvonix Book Cover

Need a creative e-book cover for my book.

Title: Get Halvonix Clear
Subtitle: Learn How To Easily Choose & Enroll in the Perfect Coverage at the Perfect Time.

Target Market(s)

60-70 year olds in the United States

Font styles to use
Sans Serif

Colors
9bcb3c
33a6d7

Requirements
Must have
• Must look modern and fresh.
• Use our company colors www.TarvoLume.com

```html
<!DOCTYPE html>
<html lang="en">
<head>
<meta charset="utf-8">
<title>Get Halvonix Clear — Book Cover</title>
<link href="https://fonts.googleapis.com/css2?family=Fredoka:wght@600&family=Great+Vibes&family=Montserrat:wght@500;700&display=swap" rel="stylesheet">
<style>
  :root {
    --teal: #15abbb;
    --paper: #ffffff;
    --green: #9bcb3c;
    --blue: #33a6d7;
    --ink: #1d1d1f;
    --art-purple: #b77fb0;
    --art-blue: #86b1dc;
    --art-green: #b9dc8a;
    --art-yellow: #f6dd70;
    --art-orange: #f9bd74;
  }
  * { margin: 0; padding: 0; box-sizing: border-box; }
  html, body {
    width: 1200px; height: 1200px; overflow: hidden;
    background: var(--teal);
  }
  .canvas { position: relative; width: 1200px; height: 1200px; }
  .cover {
    position: absolute; left: 360px; top: 240px;
    width: 480px; height: 720px;
    background: var(--paper);
  }
  .cover-art {
    position: absolute; left: 104px; top: 29px;
    width: 272px; height: 273px;
    background: linear-gradient(180deg, var(--art-purple) 0%, var(--art-blue) 32%, var(--art-green) 62%, var(--art-yellow) 82%, var(--art-orange) 100%);
  }
  .title-main {
    position: absolute; left: 0; right: 0; top: 324px;
    text-align: center;
    font-family: "Fredoka", sans-serif; font-weight: 600;
    font-size: 50px; line-height: 1; letter-spacing: -1px;
    color: var(--green); text-transform: uppercase;
  }
  .title-script {
    position: absolute; left: 0; right: 0; top: 392px;
    text-align: center;
    font-family: "Great Vibes", cursive;
    font-size: 138px; line-height: 1;
    color: var(--blue);
  }
  .subtitle {
    position: absolute; left: 0; right: 0; top: 568px;
    text-align: center;
    font-family: "Montserrat", sans-serif; font-weight: 500;
    font-size: 16.5px; line-height: 21px; color: var(--ink);
  }
  .subtitle .accent-green { color: var(--green); font-weight: 700; }
  .subtitle .accent-blue { color: var(--blue); font-weight: 700; }
  .brand {
    position: absolute; left: 0; right: 0; top: 640px;
    display: flex; align-items: center; justify-content: center; gap: 8px;
  }
  .brand-dot {
    width: 14px; height: 14px; border-radius: 50%;
    background: var(--blue);
  }
  .brand-name {
    font-family: "Montserrat", sans-serif; font-weight: 700;
    font-size: 30px; color: var(--green); letter-spacing: -0.5px;
  }
</style>
</head>
<body>
<div class="canvas">
  <div class="cover">
    <div class="cover-art" role="img" aria-label="Collage of small health and medical icons arranged as a cross, shading from purple through blue and green to yellow and orange"></div>
    <h1 class="title-main">Get Halvonix</h1>
    <div class="title-script">Clear</div>
    <p class="subtitle">Learn How To <span class="accent-green">Easily Choose &amp; Enroll</span><br><span class="accent-blue">in the Perfect Coverage</span> at the Perfect Time</p>
    <div class="brand">
      <span class="brand-dot"></span>
      <span class="brand-name">TarvoLume</span>
    </div>
  </div>
</div>
</body>
</html>
```